serious, thorough, light and simple - that's my advice and mediations

My business card should combine my logo (uploaded file) and my homepage (https://fellor-mediation.webnestsite.com).

Contact Information for Business Card

Name: Sabine Fellor di Vanti
Phone: 076 412 58 94
mail: sfellor@postkiv.ch
web: www.fellor-di-vanti.ch

```html
<!DOCTYPE html>
<html lang="de">
<head>
<meta charset="utf-8">
<title>Sabine Fellor di Vanti – Visitenkarte</title>
<link href="https://fonts.googleapis.com/css2?family=Cinzel:wght@600&display=swap" rel="stylesheet">
<style>
  :root{
    --page-bg:#e4e4e4;
    --card-white:#ffffff;
    --band-rose:#a4487a;
    --back-berry:#8b1452;
    --ink-white:#ffffff;
    --brand-gold:#a8844a;
    --brand-dot:#1f6a45;
  }
  *{margin:0;padding:0;box-sizing:border-box}
  html,body{width:1200px;height:870px;overflow:hidden;background:var(--page-bg)}
  .canvas{position:relative;width:1200px;height:870px}
  .card{position:absolute;top:115px;width:540px;height:640px;overflow:hidden;box-shadow:0 8px 24px rgba(0,0,0,.12)}
  .card--front{left:50px;background:var(--band-rose)}
  .card--back{left:610px;background:var(--back-berry)}
  .brand-area{height:294px;background:var(--card-white);display:flex;align-items:center;justify-content:center}
  .brand-line{display:flex;align-items:center;gap:16px}
  .brand-dot{width:34px;height:34px;border-radius:50%;background:var(--brand-dot)}
  .brand-name{font-family:"Cinzel",serif;font-weight:600;font-size:38px;color:var(--brand-gold);letter-spacing:.04em;white-space:nowrap}
  .contact-area{padding:36px 0 0}
  .person-name{font-family:"Cinzel",serif;font-weight:600;font-size:25px;letter-spacing:.06em;color:var(--ink-white);text-align:center;white-space:nowrap}
  .name-rule{width:405px;height:5px;background:var(--ink-white);margin:20px auto 34px}
  .contact-list{list-style:none;padding-left:118px}
  .contact-item{display:flex;align-items:center;gap:14px;height:38px;font-family:"Cinzel",serif;font-weight:600;font-size:17px;letter-spacing:.06em;color:var(--ink-white);white-space:nowrap}
  .contact-item svg{width:26px;height:26px;flex:none}
  .back-decoration{position:absolute;inset:0;background:var(--back-berry)}
</style>
</head>
<body>
<main class="canvas">
  <section class="card card--front" aria-label="Visitenkarte Vorderseite">
    <div class="brand-area">
      <div class="brand-line">
        <span class="brand-dot"></span>
        <span class="brand-name">Wege im Dialog</span>
      </div>
    </div>
    <div class="contact-area">
      <h1 class="person-name">Sabine Fellor di Vanti</h1>
      <div class="name-rule"></div>
      <ul class="contact-list">
        <li class="contact-item">
          <svg viewBox="0 0 24 24" fill="none" stroke="#fff" stroke-width="1.4"><rect x="7" y="2" width="10" height="20" rx="2"/><circle cx="12" cy="18.5" r=".8" fill="#fff"/></svg>
          076 412 58 94
        </li>
        <li class="contact-item">
          <svg viewBox="0 0 24 24" fill="none" stroke="#fff" stroke-width="1.4"><rect x="2" y="5" width="20" height="14"/><path d="M2 5l10 8 10-8"/></svg>
          sfellor@postkiv.ch
        </li>
        <li class="contact-item">
          <svg viewBox="0 0 24 24" fill="none" stroke="#fff" stroke-width="1.3"><circle cx="12" cy="12" r="10"/><ellipse cx="12" cy="12" rx="4.5" ry="10"/><path d="M2 12h20M4 7h16M4 17h16"/></svg>
          www.fellor-di-vanti.ch
        </li>
      </ul>
    </div>
  </section>
  <section class="card card--back" aria-label="Visitenkarte Rückseite">
    <div class="back-decoration" role="img" aria-label="Großes dekoratives Markenzeichen in dunklem Beerenton"></div>
  </section>
</main>
</body>
</html>
```